Online Jewellery Marketing Design Project

I need a simple colour business card with a style that can easily be transferred into grayscale and can be used for as part of the design for brochures and gift certificates.

Design to revolve around Script, Peacock feathers and the colours found in them. I would also be open to a rich purple.

The business is a small discount online jewellery and painting sales. As business improves the designs will need to be able to be used on the card backings of the jewellery, a website with cart capability and other marketing tools.

The final design should communicate inexpensive style.

I have include some of the designs I have been using while this was just a hobby. Now that it is moving towards a proper business, even if only part time, a more professional touch is required.

Industry/Entity Type

Marketing

Logo Text

Ona's Gleam Jewellery & Paintings

```html
<!DOCTYPE html>
<html lang="en">
<head>
<meta charset="utf-8">
<title>Ona's Gleam — Business Card</title>
<link rel="stylesheet" href="https://fonts.googleapis.com/css2?family=Marck+Script&family=Arimo:wght@700&display=swap">
<style>
  :root {
    --feather-deep: #10200a;
    --feather-green: #2e5814;
    --feather-teal: #1f4a3a;
    --band-veil: rgba(205, 210, 200, 0.38);
    --ink-light: #ffffff;
  }
  html, body {
    margin: 0;
    padding: 0;
    overflow: hidden;
    background: #ffffff;
  }
  .card {
    position: relative;
    width: 1200px;
    height: 741px;
    overflow: hidden;
  }
  .feather-field {
    position: absolute;
    inset: 0;
    background: linear-gradient(160deg, var(--feather-green) 0%, var(--feather-teal) 40%, var(--feather-deep) 70%, var(--feather-green) 100%);
  }
  .text-band {
    position: absolute;
    left: 0;
    top: 251px;
    width: 1200px;
    height: 462px;
    background: var(--band-veil);
  }
  .brand-name {
    position: absolute;
    left: 258px;
    top: 290px;
    margin: 0;
    font-family: "Marck Script", cursive;
    font-weight: 400;
    font-size: 94px;
    line-height: 1;
    color: var(--ink-light);
    text-shadow: 1px 1px 2px rgba(0, 0, 0, 0.4);
  }
  .brand-tagline {
    position: absolute;
    left: 344px;
    top: 392px;
    margin: 0;
    font-family: "Marck Script", cursive;
    font-size: 66px;
    line-height: 1;
    color: var(--ink-light);
    text-shadow: 2px 2px 3px rgba(0, 0, 0, 0.5);
  }
  .contact-list {
    position: absolute;
    left: 14px;
    top: 490px;
    width: 1200px;
    margin: 0;
    padding: 0;
    list-style: none;
    text-align: center;
  }
  .contact-list li {
    font-family: "Arimo", Arial, sans-serif;
    font-weight: 700;
    font-size: 29px;
    letter-spacing: 1.6px;
    line-height: 41.5px;
    color: var(--ink-light);
    text-shadow: 1px 1px 2px rgba(0, 0, 0, 0.55);
  }
</style>
</head>
<body>
  <main class="card">
    <div class="feather-field" role="img" aria-label="Close-up photograph of peacock tail feathers with blue, bronze and green eyespots filling the card"></div>
    <div class="text-band"></div>
    <h1 class="brand-name">Ona's Gleam</h1>
    <p class="brand-tagline">Jewellery &amp; Paintings</p>
    <ul class="contact-list">
      <li>www.Socialpage.com/OnasGleam</li>
      <li>www.Craftmarket.com/shop/OnasGleam</li>
      <li>myworld.bidhouse.com.au/mara4512/</li>
      <li>OnasGleam@mailbox.com</li>
    </ul>
  </main>
</body>
</html>
```